Double-sided business card needed - specific brief

We need a double sided business card designed for our company Radiant Trimline. Having lost a lot of weight myself, the back of the card needs to show my before and after pictures. It needs to cover the entire back side of the card. This might be with my two before pictures over set on top of my main after picture or in separate frames. I'll leave that to your artistic consideration. The front needs to have our logo with contact details centred below.

The cards will be printed by PRINTVEX.com and will be rectangular, 84mm x 55mm, but with ROUNDED edges. Please therefore present your designs rectangular but with rounded edges if possible.

The card should be designed in LANDSCAPE orientation.

As well as the logo, the front of the card should have the following details:

Carol Whitby
Weight Loss Motivator with 189lb personal loss
carol@radiant-trimline.example
+44 (0)7700 900418

The website is important so should perhaps be more bold than the rest:
www.radiant-trimline.example

My brand colours are: Pink #CD2366, Light Pink #FD88AD. Blue #1C9CB1, Light Blue #64C4DE

Target Market(s)

Women 30+

Contact Information for Business Card

As description above

Font styles to use
Sans Serif

Requirements
Must have
• Double sided.
• Back side entirely covered with my before and after pictures.
• You may wish to float my before pictures on top of my after picture or add them in different frames. I look forward to seeing your different suggestions.

```html
<!DOCTYPE html>
<html lang="en">
<head>
<meta charset="utf-8">
<title>Radiant Trimline – Business Card</title>
<link rel="stylesheet" href="https://fonts.googleapis.com/css2?family=Open+Sans:wght@400;600;700;800&display=swap">
<style>
  :root {
    --backdrop: #3a3a3a;
    --card-white: #ffffff;
    --ink: #111111;
    --brand-pink: #cd2366;
    --light-pink: #f48bae;
    --blue: #1c9cb1;
    --light-blue: #64c4de;
    --teal-block: #138896;
  }
  * { margin: 0; padding: 0; box-sizing: border-box; }
  html, body {
    width: 1047px; height: 1200px; overflow: hidden;
    background: radial-gradient(ellipse at 50% 45%, #444 0%, var(--backdrop) 70%, #2c2c2c 100%);
    font-family: "Open Sans", Arial, sans-serif;
  }
  .card {
    position: absolute; left: 120px; width: 755px; height: 461px;
    border-radius: 20px; overflow: hidden;
    box-shadow: 0 14px 28px rgba(0,0,0,.55);
  }

  /* Back side */
  .card-back { top: 101px; background: #1a1a1a; }
  .photo-before {
    position: absolute; left: 0; top: 0; width: 378px; height: 461px;
    background:
      radial-gradient(ellipse 95px 120px at 190px 95px, rgba(60,50,50,.85) 0%, rgba(60,50,50,.5) 55%, rgba(60,50,50,0) 100%),
      radial-gradient(ellipse 150px 230px at 200px 300px, rgba(235,235,235,.9) 0%, rgba(210,210,210,.6) 55%, rgba(210,210,210,0) 100%),
      radial-gradient(ellipse 70px 120px at 95px 250px, rgba(20,20,20,.8) 0%, rgba(20,20,20,0) 100%),
      linear-gradient(180deg, #4d4d4d 0%, #9c9c9c 14%, #bdbdbd 26%, #7a7a7a 40%, #8a8a8a 70%, #5e5e5e 100%);
  }
  .before-tint {
    position: absolute; left: 0; top: 242px; width: 378px; height: 219px;
    background: var(--brand-pink); opacity: .6; mix-blend-mode: multiply;
  }
  .before-tint-glow {
    position: absolute; left: 0; top: 242px; width: 378px; height: 219px;
    background: linear-gradient(180deg, rgba(205,35,102,.35), rgba(205,35,102,.5));
  }
  .photo-after {
    position: absolute; left: 378px; top: 0; width: 377px; height: 461px;
    background:
      radial-gradient(ellipse 70px 90px at 175px 110px, rgba(190,220,225,.55) 0%, rgba(190,220,225,0) 100%),
      radial-gradient(ellipse 130px 200px at 170px 330px, rgba(45,45,45,.9) 0%, rgba(30,30,30,0) 100%),
      linear-gradient(180deg, #7a7a7a 0%, #6a6a6a 8%, #2c2c2c 12%, #1e1e1e 60%, #111 100%);
  }
  .after-tint {
    position: absolute; left: 414px; top: 39px; width: 341px; height: 177px;
    background:
      radial-gradient(ellipse 90px 110px at 150px 90px, rgba(120,215,230,.55) 0%, rgba(120,215,230,0) 100%),
      linear-gradient(90deg, #0f7a88 0%, var(--teal-block) 50%, #0c6c78 100%);
    opacity: .92;
  }
  .label {
    position: absolute; font-weight: 800; font-size: 48px; letter-spacing: 1px;
    line-height: 1; white-space: nowrap;
  }
  .label-after {
    color: var(--light-blue);
    left: 377px; top: 205px; transform-origin: 0 0; transform: rotate(-90deg);
  }
  .label-before {
    color: var(--light-pink);
    left: 377px; top: 242px; transform-origin: 0 0; transform: rotate(90deg);
  }

  /* Front side */
  .card-front { top: 660px; height: 459px; background: var(--card-white); }
  .brand-name {
    position: absolute; left: 18px; width: 286px; top: 190px;
    text-align: center; color: var(--brand-pink);
    font-weight: 700; font-size: 30px; line-height: 1.2; letter-spacing: 1px;
  }
  .divider {
    position: absolute; left: 313px; top: 69px; width: 3px; height: 256px;
    background: var(--ink);
  }
  .contact { position: absolute; left: 337px; top: 86px; color: var(--ink); }
  .contact-name { font-weight: 700; font-size: 35px; line-height: 1; letter-spacing: .5px; }
  .contact-role { margin-top: 14px; font-size: 22px; line-height: 1.3; }
  .contact-lines { margin-top: 54px; font-size: 22px; line-height: 1.75; }
  .web-band {
    position: absolute; left: 0; bottom: 0; width: 755px; height: 110px;
    background: var(--light-pink);
    display: flex; align-items: center; justify-content: center;
    color: #fff; font-weight: 700; font-size: 33px; padding-bottom: 14px;
  }
</style>
</head>
<body>
  <section class="card card-back">
    <div class="photo-before" role="img" aria-label="Before photo: Carol standing outdoors by a fence, holding a pet"></div>
    <div class="before-tint"></div>
    <div class="before-tint-glow"></div>
    <div class="photo-after" role="img" aria-label="After photo: Carol seated on a sofa, slimmer, in a dark top"></div>
    <div class="after-tint"></div>
    <span class="label label-after">AFTER</span>
    <span class="label label-before">BEFORE</span>
  </section>

  <section class="card card-front">
    <div class="brand-name">RADIANT<br>TRIMLINE</div>
    <div class="divider"></div>
    <div class="contact">
      <div class="contact-name">CAROL WHITBY</div>
      <div class="contact-role">Weight Loss Motivator with<br>189lb personal loss</div>
      <div class="contact-lines">
        carol@radiant-trimline.example<br>
        +44 (0)7700 900418
      </div>
    </div>
    <div class="web-band">www.radiant-trimline.example</div>
  </section>
</body>
</html>
```